Securities Exam Training Banner Add for Adlane campaign

We need a banner ad design to use for a remarketing campaign in Brixel Adlane. We are a securities exam training provider that provides online training across the U.S. and Canada. Banner ad designs should be consistent in color and concept with our website: www.vornapreplabs.example.

Approved ad copy:

"Pass on your first attempt. Experience what you are missing with your current training provider."

"Pass the Tier 4 on your first attempt with our industry-leading training program. "

-High quality audio lecture.
-Interactive visual presentations.
-Comprehensive course textbook.

"We give you everything you need to pass on your first attempt."

Deliverables:

-Ad Sizes (250x250; 200x200; 468x60; 728x90; 300x250; 336x280; 120x600; 160x600)
-.gif, .jpg, .png, or .swf
-50kb or smaller

Theme:

-Design should reflect financial security, confidence in the product, and differentiation from the "rest of the industry."

Target Market(s)

People who are training for securities exams in the financial industry. e.g. people who work for Halberd Quint, Dorsey Pellham, Ashby Crane, etc..

Industry/Entity Type

Financial

Requirements
Must have
• Company Logo and phrase "The leader in securities exam prep"
Strong call to action on final screen (Buy Now).

```html
<!DOCTYPE html>
<html lang="en">
<head>
<meta charset="utf-8">
<title>Vorna Prep Labs — Securities Exam Prep Banner Set</title>
<link rel="stylesheet" href="https://fonts.googleapis.com/css2?family=Oswald:wght@500;600&family=Lato:wght@400;700&display=swap">
<style>
  :root {
    --stage: #e7e8ec;
    --navy: #0a3690;
    --royal: #1456c4;
    --stripe: #5aa8f2;
    --gold: #ffc21a;
    --gold-deep: #f29a00;
    --white: #ffffff;
    --ink: #1d1d1f;
    --logo-ink: #3a3f48;
    --photo-hi: #d9dde6;
    --photo-mid: #6e7688;
    --photo-lo: #1c1f28;
  }
  * { box-sizing: border-box; margin: 0; padding: 0; }
  html, body { width: 1200px; height: 860px; overflow: hidden; }
  body { background: var(--stage); position: relative; font-family: "Lato", Arial, sans-serif; }

  .ad { position: absolute; background: var(--white); overflow: hidden; box-shadow: 0 4px 12px rgba(0,0,0,.18); }
  .ad-field {
    position: absolute; left: 0; top: 0; z-index: 0;
    background: radial-gradient(ellipse at 30% 30%, var(--royal) 0%, var(--navy) 75%);
    border-bottom: 5px solid var(--stripe);
  }
  .portrait { position: absolute; z-index: 1; background: linear-gradient(180deg, var(--photo-hi) 0%, var(--photo-mid) 45%, var(--photo-lo) 100%); opacity: .9; }
  .headline { position: absolute; z-index: 2; white-space: nowrap; font-family: "Oswald", "Arial Narrow", sans-serif; font-weight: 600; text-transform: uppercase; color: var(--white); text-shadow: 0 2px 3px rgba(0,0,0,.45); letter-spacing: -.01em; }
  .headline .accent { color: var(--gold); display: block; }
  .perks { position: absolute; z-index: 2; white-space: nowrap; list-style: none; color: var(--white); text-shadow: 0 1px 2px rgba(0,0,0,.4); }
  .perks li { position: relative; padding-left: 1.05em; }
  .perks li::before {
    content: ""; position: absolute; left: .12em; top: .2em;
    width: .3em; height: .58em;
    border-right: .11em solid var(--gold); border-bottom: .11em solid var(--gold);
    transform: rotate(40deg);
  }
  .notch { position: absolute; z-index: 2; width: 0; height: 0; border-left: 9px solid transparent; border-right: 9px solid transparent; border-bottom: 10px solid var(--white); }
  .brand { position: absolute; z-index: 2; white-space: nowrap; display: flex; align-items: center; gap: .45em; color: var(--logo-ink); font-weight: 400; text-transform: uppercase; letter-spacing: .02em; line-height: 1.05; }
  .brand::before { content: ""; flex: none; width: 1.9em; height: 1.9em; background: var(--royal); }
  .buy {
    position: absolute; z-index: 2; display: flex; align-items: center; justify-content: center; gap: .5em;
    background: linear-gradient(180deg, #ffe066 0%, var(--gold) 45%, var(--gold-deep) 100%);
    border: 1px solid #d98a00; border-radius: 6px;
    color: var(--ink); font-weight: 700; text-decoration: none; white-space: nowrap;
    box-shadow: 0 2px 3px rgba(0,0,0,.3);
  }
  .buy svg { width: 1.3em; height: 1.3em; }

  /* 160x600 skyscraper */
  .ad-sky { left: 42px; top: 74px; width: 198px; height: 738px; }
  .ad-sky .ad-field { width: 198px; height: 603px; }
  .ad-sky .headline { left: 7px; top: 18px; font-size: 32px; line-height: 42px; }
  .ad-sky .headline .accent { font-size: 41px; line-height: 48px; }
  .ad-sky .perks { left: 10px; top: 160px; font-size: 20px; line-height: 22px; }
  .ad-sky .perks li { margin-bottom: 15px; }
  .ad-sky .portrait { left: 32px; top: 358px; width: 166px; height: 240px; }
  .ad-sky .notch { left: 12px; top: 591px; }
  .ad-sky .brand { left: 8px; top: 632px; font-size: 15px; }
  .ad-sky .buy { left: 7px; top: 682px; width: 178px; height: 44px; font-size: 21px; }

  /* 336x280 */
  .ad-rect-lg { left: 257px; top: 98px; width: 416px; height: 344px; }
  .ad-rect-lg .ad-field { width: 416px; height: 277px; }
  .ad-rect-lg .headline { left: 30px; top: 8px; font-size: 37px; line-height: 47px; }
  .ad-rect-lg .headline .accent { font-size: 47px; line-height: 54px; }
  .ad-rect-lg .perks { left: 16px; top: 164px; font-size: 18px; line-height: 22px; }
  .ad-rect-lg .perks li { margin-bottom: 5px; }
  .ad-rect-lg .portrait { left: 296px; top: 14px; width: 120px; height: 258px; }
  .ad-rect-lg .notch { left: 18px; top: 265px; }
  .ad-rect-lg .brand { left: 14px; top: 294px; font-size: 15px; }
  .ad-rect-lg .buy { left: 224px; top: 288px; width: 177px; height: 46px; font-size: 21px; }

  /* 300x250 */
  .ad-rect { left: 688px; top: 98px; width: 372px; height: 307px; }
  .ad-rect .ad-field { width: 372px; height: 240px; }
  .ad-rect .headline { left: 26px; top: 8px; font-size: 33px; line-height: 42px; }
  .ad-rect .headline .accent { font-size: 42px; line-height: 48px; }
  .ad-rect .perks { left: 13px; top: 148px; font-size: 16px; line-height: 20px; }
  .ad-rect .perks li { margin-bottom: 6px; }
  .ad-rect .portrait { left: 264px; top: 12px; width: 108px; height: 223px; }
  .ad-rect .notch { left: 20px; top: 228px; }
  .ad-rect .brand { left: 12px; top: 260px; font-size: 14px; }
  .ad-rect .buy { left: 199px; top: 252px; width: 157px; height: 44px; font-size: 19px; }

  /* 468x60 */
  .ad-banner { left: 258px; top: 479px; width: 578px; height: 71px; }
  .ad-banner .ad-field { width: 396px; height: 71px; border-bottom-width: 3px; }
  .ad-banner .headline { left: 7px; top: 5px; font-size: 30px; line-height: 34px; }
  .ad-banner .headline .accent { font-size: 19px; line-height: 22px; }
  .ad-banner .perks { left: 190px; top: 8px; font-size: 12px; line-height: 15px; }
  .ad-banner .perks li { margin-bottom: 3px; }
  .ad-banner .brand { left: 411px; top: 8px; font-size: 9px; }
  .ad-banner .buy { left: 411px; top: 35px; width: 104px; height: 28px; font-size: 12px; border-radius: 4px; }
  .ad-banner .portrait { left: 520px; top: 4px; width: 58px; height: 67px; }

  /* 728x90 */
  .ad-leader { left: 258px; top: 579px; width: 899px; height: 110px; }
  .ad-leader .ad-field { width: 621px; height: 110px; border-bottom-width: 4px; }
  .ad-leader .headline { left: 10px; top: 8px; font-size: 46px; line-height: 54px; }
  .ad-leader .headline .accent { font-size: 29px; line-height: 36px; }
  .ad-leader .perks { left: 300px; top: 12px; font-size: 19px; line-height: 24px; }
  .ad-leader .perks li { margin-bottom: 3px; }
  .ad-leader .brand { left: 640px; top: 14px; font-size: 14px; }
  .ad-leader .buy { left: 640px; top: 56px; width: 160px; height: 40px; font-size: 20px; }
  .ad-leader .portrait { left: 810px; top: 8px; width: 89px; height: 102px; }
</style>
</head>
<body>
<svg width="0" height="0" style="position:absolute" aria-hidden="true">
  <symbol id="go-arrow" viewBox="0 0 24 24">
    <circle cx="12" cy="12" r="11" fill="#2c2c30"/>
    <path d="M10 7l5 5-5 5" fill="none" stroke="#ffffff" stroke-width="2.6" stroke-linecap="round" stroke-linejoin="round"/>
  </symbol>
</svg>

<section class="ad ad-sky" aria-label="160 by 600 skyscraper ad">
  <div class="ad-field"></div>
  <div class="portrait" role="img" aria-label="Photo of a smiling businesswoman in glasses and a dark suit"></div>
  <h2 class="headline">The Leader<br>in Securities<span class="accent">Exam Prep</span></h2>
  <ul class="perks">
    <li>High quality<br>audio lecture.</li>
    <li>Interactive visual<br>presentations.</li>
    <li>Comprehensive<br>course textbook.</li>
  </ul>
  <span class="notch"></span>
  <div class="brand">Vorna Prep Labs</div>
  <a class="buy" href="#">Buy Now <svg><use href="#go-arrow"/></svg></a>
</section>

<section class="ad ad-rect-lg" aria-label="336 by 280 rectangle ad">
  <div class="ad-field"></div>
  <div class="portrait" role="img" aria-label="Photo of a smiling businesswoman in glasses and a dark suit"></div>
  <h2 class="headline">The Leader<br>in Securities<span class="accent">Exam Prep</span></h2>
  <ul class="perks">
    <li>High quality audio lecture.</li>
    <li>Interactive visual presentations.</li>
    <li>Comprehensive course textbook.</li>
  </ul>
  <span class="notch"></span>
  <div class="brand">Vorna Prep Labs</div>
  <a class="buy" href="#">Buy Now <svg><use href="#go-arrow"/></svg></a>
</section>

<section class="ad ad-rect" aria-label="300 by 250 rectangle ad">
  <div class="ad-field"></div>
  <div class="portrait" role="img" aria-label="Photo of a smiling businesswoman in glasses and a dark suit"></div>
  <h2 class="headline">The Leader<br>in Securities<span class="accent">Exam Prep</span></h2>
  <ul class="perks">
    <li>High quality audio lecture.</li>
    <li>Interactive visual presentations.</li>
    <li>Comprehensive course textbook.</li>
  </ul>
  <span class="notch"></span>
  <div class="brand">Vorna Prep Labs</div>
  <a class="buy" href="#">Buy Now <svg><use href="#go-arrow"/></svg></a>
</section>

<section class="ad ad-banner" aria-label="468 by 60 banner ad">
  <div class="ad-field"></div>
  <div class="portrait" role="img" aria-label="Photo of a smiling businesswoman in glasses and a dark suit"></div>
  <h2 class="headline">The Leader in<span class="accent">Securities Exam Prep</span></h2>
  <ul class="perks">
    <li>High quality audio lecture.</li>
    <li>Interactive visual presentations.</li>
    <li>Comprehensive course textbook.</li>
  </ul>
  <div class="brand">Vorna Prep Labs</div>
  <a class="buy" href="#">Buy Now <svg><use href="#go-arrow"/></svg></a>
</section>

<section class="ad ad-leader" aria-label="728 by 90 leaderboard ad">
  <div class="ad-field"></div>
  <div class="portrait" role="img" aria-label="Photo of a smiling businesswoman in glasses and a dark suit"></div>
  <h2 class="headline">The Leader in<span class="accent">Securities Exam Prep</span></h2>
  <ul class="perks">
    <li>High quality audio lecture.</li>
    <li>Interactive visual presentations.</li>
    <li>Comprehensive course textbook.</li>
  </ul>
  <div class="brand">Vorna Prep Labs</div>
  <a class="buy" href="#">Buy Now <svg><use href="#go-arrow"/></svg></a>
</section>
</body>
</html>
```